Flyer-Design für Ofenservice Firma
Zielgruppe
Die Firma hat als Kerngeschäft Wartung, Reinigung, Reparatur und Inbetriebnahme von Öfen und Kaminen aller Art. Der Fokus liegt dabei auf Pelletöfen. Die Firma versteht sich als zuverlässiger Dienstleister mit gutem Preisleistungsverhältnis. Zielgruppe sind hauptsächlich private Bewohner von Einfamilienhäusern in der ländlichen Gegend (Hessen)
Aufgabenstellung
Zur Bekanntmachung nach Neugründung soll ein Faltflyer gestaltet werden mit insgesamt 6 Bereichen. Die Informationen, welche auf den Flyer sollen, entnehmen Sie bitte dem Entwurf (flyer.pdf). Dieser stellt nur eine erste Idee dar und darf gerne nach Belieben verändert bzw. neu gestaltet werden. Die enthaltenen Informationen, sollten im Großen und Ganzen aber beibehalten werden. Schön wäre evtl. auch eine Hervorhebung der Preise, da wir Preisführer im Markt sind. Auch die Bilder unseres Teams sollen in den Flyer integriert sein. Auf Anfrage kann ich auch gerne weitere Kamin- und Ofenfotos zur Verfügung stellen, für welche ich die Nutzungsrechte habe. Falls Sie weitere Informationen benötigen oder Fragen haben, kommen Sie gerne auf mich zu. Die Bilder dürfen gerne etwas ausgeschnitten werden. Es geht in erster Linie darum, dass die Kunden erkennen, welche Art von Ofen sie zu Hause haben.

```html
<!DOCTYPE html>
<html lang="de">
<head>
<meta charset="utf-8">
<title>Wartung von Öfen – Preise</title>
<link rel="stylesheet" href="https://fonts.googleapis.com/css2?family=Josefin+Sans:wght@700&family=Arimo:wght@400;700&display=swap">
<style>
  :root {
    --orange: #e0602a;
    --orange-deep: #d8561f;
    --peach: #f3c7a9;
    --ink: #3d4756;
    --white: #ffffff;
  }
  * { box-sizing: border-box; margin: 0; padding: 0; }
  html, body { width: 1200px; height: 805px; overflow: hidden; background: var(--orange); }
  .flyer { position: relative; width: 1200px; height: 805px; background: var(--orange); font-family: "Arimo", Arial, sans-serif; }

  .services { position: absolute; left: 0; top: 0; width: 1200px; height: 349px; background: var(--orange); }
  .service { position: absolute; top: 54px; width: 360px; color: var(--white); }
  .service--pellet { left: 20px; }
  .service--wood { left: 415px; }
  .service--tile { left: 817px; }

  .service__title {
    font-family: "Josefin Sans", sans-serif;
    font-weight: 700;
    font-size: 17px;
    line-height: 19px;
    letter-spacing: 0.4px;
    text-transform: uppercase;
    margin-bottom: 18px;
  }
  .service__list { list-style: none; font-size: 13px; line-height: 15.5px; }
  .service__list li { position: relative; padding-left: 14px; }
  .service__list li::before { content: "•"; position: absolute; left: 0; top: 0; }

  .prices { position: absolute; left: 0; top: 349px; width: 1200px; height: 141px; background: var(--peach); color: var(--ink); }
  .price { position: absolute; top: 10px; font-size: 12.5px; line-height: 15px; font-weight: 700; }
  .price--pellet { left: 23px; }
  .price--wood { left: 420px; }
  .price--tile { left: 817px; }
  .price__label { font-weight: 700; }
  .price__note { position: absolute; right: 24px; bottom: 9px; font-size: 10.5px; font-weight: 700; }

  .strip { position: absolute; left: 0; top: 490px; width: 1200px; height: 21px; background: var(--orange); }

  .photos { position: absolute; left: 0; top: 511px; width: 1200px; height: 294px; }
  .photo { position: absolute; top: 0; height: 294px; }
  .photo--pellet { left: 0; width: 395px; background: linear-gradient(90deg, #c9b39a 0%, #e9e7e3 40%, #f3f1ee 60%, #bdb7ae 100%); }
  .photo--wood { left: 395px; width: 403px; background: linear-gradient(90deg, #2a3444 0%, #3a4658 40%, #5a4a3c 75%, #8e8577 100%); }
  .photo--tile { left: 798px; width: 402px; background: linear-gradient(135deg, #6a4a2a 0%, #b58a52 45%, #d9c28a 65%, #4a3425 100%); }
</style>
</head>
<body>
<main class="flyer">
  <section class="services">
    <article class="service service--pellet">
      <h2 class="service__title">Wartung<br>von<br>Palletöfen</h2>
      <ul class="service__list">
        <li>Reinigung von der Sichtscheibe, Brenntopf, Topfhalter, Zwischenboden, gesamter Feuerraum, sämtliche Rauchgaszüge, Aschebehälter, Luftmengensensors und des Saugzuggebläses</li>
        <li>Überprüfung des Luftmengensensors, der elektrischen Zündung, aller Dichtungen und des Temperaturwächter</li>
        <li>Probelauf des Gerätes</li>
      </ul>
    </article>
    <article class="service service--wood">
      <h2 class="service__title">Wartung von<br>Scheitholzöfen<br>Heizkassetten<br>Brennzellen<br>Holz- und Küchenherde</h2>
      <ul class="service__list">
        <li>Reinigung von der Schamott Verkleidung, Sichtscheibe, dem Zwischenboden, gesamter Feuerraum, sowie sämtlichen Rauchgaszügen und des Aschebehälters</li>
        <li>Reinigung der Abgasrohre (bis 2 m gestreckte Länge)</li>
        <li>Überprüfung der Dichtungen</li>
        <li>Probelauf des Gerätes</li>
      </ul>
    </article>
    <article class="service service--tile">
      <h2 class="service__title">Wartung<br>von<br>Grund-/Kachelöfen</h2>
      <ul class="service__list">
        <li>Reinigung von der Schamott Verkleidung, Sichtscheibe, dem Zwischenboden, gesamter Feuerraum, sowie sämtlichen Rauchgaszügen und des Aschebehälters</li>
        <li>Reinigung der Abgasrohre (bis 2 m gestreckte Länge)</li>
        <li>Überprüfung der Dichtungen</li>
        <li>Probelauf des Gerätes</li>
      </ul>
    </article>
  </section>

  <section class="prices">
    <div class="price price--pellet">
      <p class="price__label">Preise</p>
      <p>Mit Wartungsvertrag: 140 €</p>
      <p>Ohne Wartungsvertrag: 180 €</p>
    </div>
    <div class="price price--wood">
      <p class="price__label">Preise</p>
      <p>Mit Wartungsvertrag: 80€</p>
      <p>Ohne Wartungsvertrag: 110€</p>
    </div>
    <div class="price price--tile">
      <p class="price__label">Preise</p>
      <p>Kachelofen mit bis zu 4 Öffnungen</p>
      <p>Mit Wartungsvertrag: 350€</p>
      <p>Ohne Wartungsvertrag: 390€</p>
      <p>Kachelofen mit nachgeschalteter Heizfläche</p>
      <p>Mit Wartungsvertrag: 250€</p>
      <p>Ohne Wartungsvertrag: 290€</p>
    </div>
    <p class="price__note">Alle Preise inkl. MwSt.</p>
  </section>

  <div class="strip"></div>

  <section class="photos">
    <div class="photo photo--pellet" role="img" aria-label="Weißer Pelletofen mit brennendem Feuer in einem hellen Raum"></div>
    <div class="photo photo--wood" role="img" aria-label="Eck-Kaminofen mit Holzfeuer in einem dunklen Wohnzimmer mit Sofa"></div>
    <div class="photo photo--tile" role="img" aria-label="Rustikale Küche mit Holzherd, Kronleuchter und Holztisch"></div>
  </section>
</main>
</body>
</html>
```